A Hair, Beauty and Nails Wholesalers Needs a Business Card Design

We need a business card design for our company which is being passed from parents to daughter, so we wont to re-launch the company with an updated, modern, sophisticated, elegant, chic and fresh look which still incorporates the original colour scheme of Hot Pink, Dark Grey and White. The original logo which is attached can be used on the card but we would like to see some designs with the logo and some without, as we have not yet decided if we want the logo on the card. The name of our company is 'RM's Distributors' and the name of our website is RM's GlowandPolish.example.au. We specialise in supplying a massive range of Hair, Beauty and Nail products to the industry. We are based in QLD, Australia but ship many orders via our website all across Australia.

Industry/Entity Type

Business

```html
<!DOCTYPE html>
<html lang="en">
<head>
<meta charset="utf-8">
<title>RM's Distributors – Business Card</title>
<link href="https://fonts.googleapis.com/css2?family=Arimo:wght@400&family=Roboto+Slab:wght@400&display=swap" rel="stylesheet">
<style>
  :root {
    --hot-pink: #d8137c;
    --dark-grey: #3a3a3a;
    --mid-grey: #6b6b6b;
    --white: #ffffff;
    --backdrop: #8d8f94;
  }
  html, body {
    margin: 0;
    width: 1200px;
    height: 960px;
    overflow: hidden;
    background: var(--backdrop);
  }
  .stage {
    position: relative;
    width: 1200px;
    height: 960px;
  }
  .card {
    position: absolute;
    width: 560px;
    height: 336px;
    background: var(--white);
    border-radius: 8px 48px 8px 48px;
    overflow: hidden;
    box-shadow: 0 14px 30px rgba(0,0,0,0.35);
    font-family: "Arimo", Arial, sans-serif;
  }
  /* Front */
  .card--front { left: 80px; top: 80px; }
  .brand {
    position: absolute;
    display: flex;
    align-items: center;
    gap: 12px;
  }
  .brand__dot {
    width: 34px;
    height: 34px;
    border-radius: 50%;
    background: var(--hot-pink);
  }
  .brand__name {
    color: var(--hot-pink);
    font-size: 26px;
    font-weight: 400;
    letter-spacing: 0.2px;
  }
  .card--front .brand { left: 0; right: 0; top: 72px; justify-content: center; }
  .front__rule {
    position: absolute;
    left: 0; right: 0;
    top: 186px;
    height: 2px;
    background: var(--hot-pink);
  }
  .front__band {
    position: absolute;
    left: 0; right: 0;
    top: 194px; bottom: 0;
    background: var(--hot-pink);
    display: flex;
    align-items: center;
    justify-content: center;
  }
  .front__title {
    font-family: "Roboto Slab", Georgia, serif;
    color: var(--white);
    font-size: 36px;
    font-weight: 400;
    letter-spacing: 1px;
  }
  /* Back */
  .card--back { left: 560px; top: 520px; }
  .card--back .brand { left: 40px; top: 110px; }
  .person {
    position: absolute;
    right: 40px;
    top: 44px;
    text-align: right;
  }
  .person__name {
    color: var(--hot-pink);
    font-size: 25px;
  }
  .person__role {
    color: var(--dark-grey);
    font-size: 15px;
    margin-top: 2px;
    padding-bottom: 4px;
    border-bottom: 1px solid var(--dark-grey);
  }
  .back__divider {
    position: absolute;
    left: 30px;
    width: 300px;
    top: 206px;
    height: 1px;
    background: var(--dark-grey);
  }
  .contacts {
    position: absolute;
    left: 40px;
    top: 220px;
    margin: 0;
    padding: 0;
    list-style: none;
    color: var(--mid-grey);
    font-size: 15px;
    line-height: 21px;
  }
  .contacts li { display: flex; align-items: flex-start; gap: 10px; }
  .contacts svg { flex: none; margin-top: 4px; }
  .web {
    position: absolute;
    right: 40px;
    top: 224px;
    display: flex;
    align-items: center;
    gap: 8px;
    color: var(--mid-grey);
    font-size: 15px;
  }
  .web__accent { color: var(--hot-pink); }
</style>
</head>
<body>
<main class="stage">
  <section class="card card--front" aria-label="Business card front">
    <div class="brand">
      <span class="brand__dot"></span>
      <span class="brand__name">RM's GlowandPolish</span>
    </div>
    <div class="front__rule"></div>
    <div class="front__band">
      <h1 class="front__title">RM's Distributors</h1>
    </div>
  </section>

  <section class="card card--back" aria-label="Business card back">
    <div class="person">
      <div class="person__name">Danielle Harper</div>
      <div class="person__role">Manager</div>
    </div>
    <div class="brand">
      <span class="brand__dot"></span>
      <span class="brand__name">RM's GlowandPolish</span>
    </div>
    <div class="back__divider"></div>
    <ul class="contacts">
      <li>
        <svg width="12" height="12" viewBox="0 0 12 12" aria-hidden="true"><path d="M2 1 L4 1 L5 4 L3.6 5 Q5 7.5 7 8.4 L8 7 L11 8 L11 10 Q10 11 8.5 11 Q2.5 9.5 1 3.5 Q1 2 2 1Z" fill="var(--hot-pink)"/></svg>
        <span>(07) 4000 1234</span>
      </li>
      <li>
        <svg width="12" height="12" viewBox="0 0 12 12" aria-hidden="true"><rect x="0.5" y="2" width="11" height="8" fill="var(--hot-pink)"/><path d="M0.5 2 L6 6.5 L11.5 2" stroke="var(--white)" fill="none"/></svg>
        <span>admin@glowandpolish.example.au</span>
      </li>
      <li>
        <svg width="12" height="12" viewBox="0 0 12 12" aria-hidden="true"><path d="M6 11.5 Q1.5 6.5 1.5 4.5 A4.5 4.5 0 0 1 10.5 4.5 Q10.5 6.5 6 11.5Z" fill="var(--hot-pink)"/><circle cx="6" cy="4.5" r="1.6" fill="var(--white)"/></svg>
        <span>27 Example Street<br>SPRINGVALE, QLD, 4000</span>
      </li>
    </ul>
    <div class="web">
      <svg width="12" height="12" viewBox="0 0 12 12" aria-hidden="true"><circle cx="6" cy="6" r="5.5" fill="var(--hot-pink)"/><path d="M0.5 6 H11.5 M6 0.5 Q3 6 6 11.5 M6 0.5 Q9 6 6 11.5" stroke="var(--white)" stroke-width="0.8" fill="none"/></svg>
      <span>www.<span class="web__accent">glowandpolish</span>.example.au</span>
    </div>
  </section>
</main>
</body>
</html>
```